Business card for Eyelash extension salon in Beverly Hills,California USA

We need new business card for our salon in Beverly Hills. The salon name is 'Lumarra' . We would like to have...Business name: Lumarra Name of person: will provide later Address 6128 N.Corbel Ridge Blvd Beverly Hills , CA 90210 Phone: will provide later (Text only) Web: www.lumarrastudio-example.com Pictogrid icon, Friendvale icon follow us for seasonal campaign and news @lumarrastudioexample Design should look elegant, high-end, clean, simple, cohesive with my brand. Please refer my brand board. Business name color will be metallic bronzy color. Im thinking grey background or white background. Thanks

Target Market(s)

25-35. Gender neutral. People who are in Entertainment business industry.
This is High-end Eyelash extension salon in Beverly Hills

Industry/Entity Type

Beauty Salon

Contact Information for Business Card

Business name: Lumarra
Name of person: will provide later
Address 6128 N.Corbel Ridge Blvd Beverly Hills , CA 90210
Phone: will provide later (Text only)
Web: www.lumarrastudio-example.com
Pictogrid icon, Friendvale icon
follow us for seasonal campaign and news @lumarrastudioexample

Requirements
Must have
• Beautiful, elegant, clean and simple look but very attractive and modern
Should not have
• We don't like too clutter, too busy designs.

```html
<!DOCTYPE html>
<html lang="en">
<head>
<meta charset="utf-8">
<title>Lumarra Business Card</title>
<link rel="stylesheet" href="https://fonts.googleapis.com/css2?family=Playfair+Display:wght@400;600&family=Libre+Caslon+Text:wght@400&display=swap">
<style>
  :root {
    --stage: #272727;
    --card: #1c1c1c;
    --bronze: #8a6a4f;
    --ink-light: #f2efea;
    --ink-muted: #b9a48f;
  }
  * { box-sizing: border-box; margin: 0; padding: 0; }
  html, body { width: 1152px; height: 1200px; overflow: hidden; }
  body {
    background: var(--stage);
    position: relative;
    font-family: "Libre Caslon Text", Georgia, serif;
    color: var(--ink-light);
  }
  .card {
    position: absolute;
    width: 520px;
    height: 520px;
    background: var(--card);
    box-shadow: 0 18px 40px rgba(0,0,0,0.35);
  }
  .card--front { left: 80px; top: 70px; }
  .card--back {
    left: 552px; top: 620px;
    border: 16px solid var(--bronze);
  }
  .brand-name {
    font-family: "Playfair Display", Georgia, serif;
    font-weight: 400;
    color: var(--bronze);
    letter-spacing: 2px;
  }
  .card--front .brand-name {
    position: absolute;
    left: 0; right: 0; top: 150px;
    text-align: center;
    font-size: 82px;
  }
  .follow-band {
    position: absolute;
    left: 0; right: 0; top: 326px;
    height: 46px;
    background: var(--bronze);
    display: flex; align-items: center; justify-content: center;
    font-size: 19px;
    letter-spacing: 0.5px;
    color: var(--ink-light);
  }
  .social-row {
    position: absolute;
    left: 0; right: 0; top: 396px;
    display: flex; justify-content: center; align-items: center; gap: 16px;
    font-size: 15px;
  }
  .social-name { color: var(--ink-muted); }
  .social-handle { color: var(--ink-light); }
  .person {
    position: absolute; left: 40px; top: 40px;
  }
  .person-name {
    font-family: "Playfair Display", Georgia, serif;
    font-weight: 600;
    font-size: 32px;
    color: var(--bronze);
    line-height: 1.1;
  }
  .person-title { font-size: 15px; margin-top: 4px; }
  .contact-list {
    list-style: none;
    position: absolute; left: 40px; top: 150px;
    font-size: 15px;
  }
  .contact-list li { display: flex; align-items: center; gap: 12px; margin-bottom: 8px; }
  .contact-list svg { width: 15px; height: 15px; fill: var(--bronze); flex: none; }
  .card--back .brand-name {
    position: absolute; right: 40px; top: 250px;
    font-size: 60px;
  }
  .address {
    position: absolute; right: 36px; bottom: 36px;
    text-align: right;
    font-size: 15px;
    line-height: 1.3;
  }
</style>
</head>
<body>
  <section class="card card--front">
    <p class="brand-name">Lumarra</p>
    <div class="follow-band">follow us for seasonal campaign and news</div>
    <div class="social-row">
      <span class="social-name">Friendvale</span>
      <span class="social-name">Pictogrid</span>
      <span class="social-handle">@lumarrastudioexample</span>
    </div>
  </section>

  <section class="card card--back">
    <div class="person">
      <p class="person-name">Maren Solvik</p>
      <p class="person-title">Executive Director</p>
    </div>
    <ul class="contact-list">
      <li>
        <svg viewBox="0 0 24 24" aria-hidden="true"><path d="M6.6 10.8a15.2 15.2 0 0 0 6.6 6.6l2.2-2.2c.3-.3.7-.4 1-.2 1.1.4 2.3.6 3.6.6.6 0 1 .4 1 1V20c0 .6-.4 1-1 1A17 17 0 0 1 3 4c0-.6.4-1 1-1h3.5c.6 0 1 .4 1 1 0 1.3.2 2.5.6 3.6.1.3 0 .7-.2 1z"/></svg>
        <span>123 456 7890</span>
      </li>
      <li>
        <svg viewBox="0 0 24 24" aria-hidden="true"><path d="M2 5h20v14H2z M3.5 6.5 12 13l8.5-6.5" fill-rule="evenodd"/><path d="M2 5l10 8 10-8v2l-10 8L2 7z" fill="#1c1c1c"/></svg>
        <span>info@lumarra-example.com</span>
      </li>
      <li>
        <svg viewBox="0 0 24 24" aria-hidden="true"><path d="M12 2a10 10 0 1 0 0 20 10 10 0 0 0 0-20zm6.9 6h-3a15 15 0 0 0-1.3-3.9A8 8 0 0 1 18.9 8zM12 4c.8 1.2 1.5 2.5 1.9 4h-3.8c.4-1.5 1.1-2.8 1.9-4zM4.3 14a8 8 0 0 1 0-4h3.4a16 16 0 0 0 0 4zm.8 2h3a15 15 0 0 0 1.3 3.9A8 8 0 0 1 5.1 16zm3-8h-3a8 8 0 0 1 4.3-3.9A15 15 0 0 0 8.1 8zM12 20c-.8-1.2-1.5-2.5-1.9-4h3.8c-.4 1.5-1.1 2.8-1.9 4zm2.3-6H9.7a14 14 0 0 1 0-4h4.6a14 14 0 0 1 0 4zm.3 5.9a15 15 0 0 0 1.3-3.9h3a8 8 0 0 1-4.3 3.9zm1.7-5.9a16 16 0 0 0 0-4h3.4a8 8 0 0 1 0 4z"/></svg>
        <span>www.lumarrastudio-example.com</span>
      </li>
    </ul>
    <p class="brand-name">Lumarra</p>
    <address class="address" style="font-style:normal">6128 N.Corbel Ridge Blvd Beverly Hills<br>CA 90210</address>
  </section>
</body>
</html>
```